Wordpress Design Project

I now need a Wordpress theme for my new business.
The business offers consultancy on Information Management, Knowledge Management, Records Management and Document Management.
The winning designer must be able to set up the site for me on my webspace provided by Kestrowave Hosting, or talk me through how to do this.
I already have a logo designed which you can see by viewing my profile on here. I am happy to send copies of the original artwork to bidders.
I recently sold my interest in a very similar business, and want a website similar to (but not the same as) the previous company (who are now my competition!) This website can be viewed at www.trulvanworks.example
Categories will be similar, but I would like everything to be as configurable as possible.
I have a strong preference for clean unfussy design.
I want original design please. Please no templates from free to use sites with stock images... no jigsaw pictures!!!!
Love this one... http://www.quellimar.example/
Please get in touch with any questions.
Reason: All of these are too generic (brief says no jigsaw puzzle images), or have copied TKW which is the COMPETITION - so I don't want the site to look like theirs
Reason: Please keep trying people
Business
Business

```html
<!DOCTYPE html>
<html lang="en">
<head>
<meta charset="utf-8">
<title>Carrowmere Professional Services</title>
<link rel="stylesheet" href="https://fonts.googleapis.com/css2?family=Arimo:ital,wght@0,400;0,700;1,700&family=Lora:ital@1&family=Questrial&family=Tinos&display=swap">
<style>
:root{
  --navy:#1d4a86;
  --blue:#2466a8;
  --sky:#4b9fd8;
  --page:#f7f7f5;
  --band:#efeeeb;
  --panel:#e9e9e9;
  --rule:#d4d4d4;
  --text:#666;
  --dark:#222;
  --btn-top:#5d7e96;
  --btn-bot:#2f4d63;
}
*{box-sizing:border-box;margin:0;padding:0}
html,body{width:1004px;height:1200px;overflow:hidden}
body{background:var(--page);position:relative;font-family:Arimo,Arial,sans-serif;color:var(--text)}
.abs{position:absolute}
.topbar{left:0;top:0;width:1004px;height:4px;background:var(--navy)}
.brand{left:134px;top:12px;display:flex;align-items:center;gap:9px}
.brand-dot{width:44px;height:44px;border-radius:50%;background:var(--navy)}
.brand-name{font-family:Questrial,sans-serif;color:var(--navy);font-size:21px;letter-spacing:2px;line-height:1}
.brand-name small{display:block;font-size:7px;letter-spacing:2.4px;margin-top:3px}
.nav a{position:absolute;top:28px;font-family:Lora,serif;font-style:italic;font-size:12px;color:var(--navy);text-decoration:none;letter-spacing:.6px}
.nav a.current{left:425px;top:22px;width:53px;height:29px;background:linear-gradient(#6cb4e8,#3a8ed0);border:1px solid #2d6ea8;color:#fff;text-align:center;line-height:27px}
.hero{left:132px;top:70px;width:723px;height:313px;border:1px solid #d8d8d6;background:#f2f1ee}
.hero-inner{left:4px;top:4px;width:713px;height:303px;border:1px solid #dadad8}
.hero h1{position:absolute;right:408px;top:52px;width:300px;text-align:right;font-family:Questrial,sans-serif;font-weight:400;font-size:38px;line-height:46px;color:var(--navy)}
.hero p{position:absolute;right:408px;top:158px;width:280px;text-align:right;font-family:Questrial,sans-serif;font-size:15px;line-height:22px;color:var(--dark)}
.hero-art{position:absolute;left:327px;top:6px;width:364px;height:292px;border-radius:40%;background:radial-gradient(ellipse at 60% 45%,#9fd0f2 0%,#cfe6f6 45%,rgba(242,241,238,0) 72%)}
.hero-shadow{left:144px;top:392px;width:696px;height:8px;background:radial-gradient(ellipse at 50% 0,rgba(0,0,0,.45),rgba(0,0,0,0) 70%)}
.band{left:0;top:408px;width:1004px;height:262px;background:var(--band);border-top:1px solid #e4e3e0;border-bottom:2px solid #e1e0dc}
.service{position:absolute;top:434px;width:210px}
.service h3{font-family:Questrial,sans-serif;font-weight:400;font-variant:small-caps;font-size:11px;color:var(--blue);letter-spacing:.6px;white-space:nowrap}
.service .icon{position:absolute;left:0;top:32px;width:66px;height:58px;border-radius:8px;background:linear-gradient(#f4f4f4,#d8d8d8)}
.service .lead{position:absolute;left:78px;top:32px;width:130px;font-weight:700;font-style:italic;font-size:8.6px;line-height:14px;color:#555;text-align:justify}
.service .body{position:absolute;left:0;top:98px;width:209px;font-size:8.4px;line-height:12.5px;text-align:justify}
.btn{position:absolute;display:block;background:linear-gradient(var(--btn-top),var(--btn-bot));color:#fff;border:1px solid #243c4f;border-radius:2px;font-size:8.6px;text-align:center;text-decoration:none}
.service .btn{left:134px;top:181px;width:73px;height:18px;line-height:16px}
.arrow{top:516px;width:18px;height:18px}
h2.section{position:absolute;font-family:Questrial,sans-serif;font-weight:400;font-size:14.5px;color:#444;letter-spacing:.4px}
.rule{position:absolute;height:1px;background:var(--rule)}
.about-text{left:132px;top:743px;width:340px;font-size:8.8px;line-height:14.6px}
.about-text p+p{margin-top:14.6px}
.video{left:540px;top:738px;width:275px;height:139px;background:#000}
.controls{position:absolute;left:11px;top:108px;width:253px;height:19px;background:linear-gradient(#2a2a2a,#151515);border-radius:2px}
.footer{left:114px;top:925px;width:741px;height:205px;background:var(--panel);border-radius:3px}
.footer h4{position:absolute;font-family:Tinos,serif;font-weight:400;font-size:12px;color:#777}
.links a{position:absolute;font-size:8px;color:#666;text-decoration:none}
.post{position:absolute;left:274px;width:190px;font-size:8.8px;line-height:15px;color:#777;padding-left:8px}
.post::before{content:"•";position:absolute;left:0}
.social span{position:absolute;top:173px;width:18px;height:18px;border-radius:3px;background:#a8a8a8}
.field{position:absolute;left:511px;width:190px;background:#fff;border:1px solid #cfcfcf;border-radius:3px;font-size:8.8px;color:#777;padding:5px 5px}
.footer .btn{left:634px;top:173px;width:68px;height:17px;line-height:15px;font-size:9px}
.copyright{left:0;top:1145px;width:930px;text-align:center;font-size:7.6px;color:#777}
</style>
</head>
<body>
<div class="abs topbar"></div>

<header>
  <div class="abs brand"><span class="brand-dot"></span><span class="brand-name">CARROWMERE<small>PROFESSIONAL SERVICES</small></span></div>
  <nav class="nav">
    <a class="current" href="#">Home</a>
    <a href="#" style="left:494px">About Us</a>
    <a href="#" style="left:571px">News</a>
    <a href="#" style="left:627px">Technology</a>
    <a href="#" style="left:720px">Services</a>
    <a href="#" style="left:793px">Contact Us</a>
  </nav>
</header>

<section class="abs hero">
  <div class="abs hero-inner">
    <h1>Standard Lorem Ipsum</h1>
    <p>Lorem ipsum dolor sit amet, consectetur adipisicing elit, sed do eiusmod tempor incididunt ut labore et dolore magna aliqua.</p>
    <div class="hero-art" role="img" aria-label="Blue glossy puzzle piece illustration"></div>
  </div>
</section>
<div class="abs hero-shadow"></div>

<section class="abs band"></section>
<svg class="abs arrow" style="left:110px" viewBox="0 0 18 18"><circle cx="9" cy="9" r="8" fill="#fff" stroke="#2d5a8a" stroke-width="1.6"/><path d="M11 5 6 9l5 4z" fill="#2d5a8a"/></svg>
<svg class="abs arrow" style="left:854px" viewBox="0 0 18 18"><circle cx="9" cy="9" r="8" fill="#fff" stroke="#2d5a8a" stroke-width="1.6"/><path d="M7 5l5 4-5 4z" fill="#2d5a8a"/></svg>

<article class="service" style="left:150px">
  <h3>Records &amp; Information Management</h3>
  <div class="icon" role="img" aria-label="Monitor icon"></div>
  <p class="lead">Lorem ipsum dolor sit amet, consectetur adipisicing elit, sed do eiusmod tempor incididunt ut labore et dolore magna aliqua.</p>
  <p class="body">Ut enim ad minim veniam, quis nostrud exercitation ullamco laboris nisi ut aliquip ex ea commodo consequat. Duis aute irure dolor in reprehenderit in voluptate velit esse cillum dolore eu fugiat nulla pariatur. Excepteur sint occaecat cupidatat non proident, sunt in culpa qui officia deserunt mollit anim id est laborum.</p>
  <a class="btn" href="#">LEARN MORE</a>
</article>
<article class="service" style="left:391px">
  <h3>Business Content Analysis</h3>
  <div class="icon" style="border-radius:50%" role="img" aria-label="Pie chart icon"></div>
  <p class="lead">Lorem ipsum dolor sit amet, consectetur adipisicing elit, sed do eiusmod tempor incididunt ut labore et dolore magna aliqua.</p>
  <p class="body">Ut enim ad minim veniam, quis nostrud exercitation ullamco laboris nisi ut aliquip ex ea commodo consequat. Duis aute irure dolor in reprehenderit in voluptate velit esse cillum dolore eu fugiat nulla pariatur. Excepteur sint occaecat cupidatat non proident, sunt in culpa qui officia deserunt mollit anim id est laborum.</p>
  <a class="btn" href="#">LEARN MORE</a>
</article>
<article class="service" style="left:630px">
  <h3>Data Compliance Audit</h3>
  <div class="icon" role="img" aria-label="Notepad and pencil icon"></div>
  <p class="lead">Lorem ipsum dolor sit amet, consectetur adipisicing elit, sed do eiusmod tempor incididunt ut labore et dolore magna aliqua.</p>
  <p class="body">Ut enim ad minim veniam, quis nostrud exercitation ullamco laboris nisi ut aliquip ex ea commodo consequat. Duis aute irure dolor in reprehenderit in voluptate velit esse cillum dolore eu fugiat nulla pariatur. Excepteur sint occaecat cupidatat non proident, sunt in culpa qui officia deserunt mollit anim id est laborum.</p>
  <a class="btn" href="#">LEARN MORE</a>
</article>

<h2 class="section" style="left:132px;top:705px">About Our Company</h2>
<div class="rule" style="left:132px;top:730px;width:338px"></div>
<div class="abs about-text">
  <p>Lorem ipsum dolor sit amet, consetetur sadipscing elitr, sed diam nonumy eirmod tempor invidunt ut labore et dolore magna alrat, sed dia voluptua.</p>
  <p>At vero eos et accusam et justo duo dolores et ea rebum. Stet clita kasd gubergrenno sea takimata sanctus est Lorem ipsum dolor sit amet. Lorem ipsum dolor sit amet, consetetur sadipscing elitr, sed diam nonumy eirmod tempor invidunt ut labore et dolore magna aliquyam erat, sed diam voluptua. At vero eos et accusam et justo duo dolores et ea rebum.</p>
</div>

<h2 class="section" style="left:528px;top:702px">How We Work</h2>
<div class="rule" style="left:524px;top:727px;width:310px"></div>
<div class="abs video">
  <svg class="controls" viewBox="0 0 253 19">
    <path d="M9 6l5 3.5-5 3.5z" fill="#ddd"/>
    <rect x="24" y="0" width="1" height="19" fill="#444"/>
    <rect x="28" y="7.5" width="160" height="4" rx="2" fill="#333"/>
    <rect x="28" y="7.5" width="110" height="4" rx="2" fill="#3d86cc"/>
    <rect x="196" y="0" width="1" height="19" fill="#444"/>
    <path d="M203 8h2l3-2.5v8L205 11h-2z" fill="#ddd"/>
    <rect x="212" y="7.5" width="26" height="4" rx="2" fill="#3d86cc"/>
  </svg>
</div>

<footer class="abs footer">
  <h4 style="left:38px;top:12px">Quick Link</h4>
  <div class="rule" style="left:38px;top:30px;width:192px"></div>
  <div class="links">
    <a style="left:43px;top:39px">Company</a><a style="left:162px;top:39px">Company</a>
    <a style="left:43px;top:55px">Services</a><a style="left:162px;top:55px">Services</a>
    <a style="left:43px;top:72px">Technology</a><a style="left:162px;top:72px">Technology</a>
    <a style="left:43px;top:89px">News</a><a style="left:162px;top:89px">News</a>
    <a style="left:43px;top:105px">Clients' Speak</a><a style="left:162px;top:105px">Clients' Speak</a>
  </div>
  <h4 style="left:38px;top:137px">Connect with Us:</h4>
  <div class="rule" style="left:38px;top:157px;width:192px"></div>
  <div class="social">
    <span style="left:39px"></span><span style="left:75px"></span><span style="left:111px"></span><span style="left:147px"></span><span style="left:183px"></span>
  </div>

  <h4 style="left:274px;top:12px">Recent Post</h4>
  <div class="rule" style="left:274px;top:30px;width:192px"></div>
  <p class="post" style="top:37px">Lorem ipsum dolor sit amet, consetetur sadip scing elitr, sed diam nonumy</p>
  <div class="rule" style="left:274px;top:75px;width:192px"></div>
  <p class="post" style="top:80px">Lorem ipsum dolor sit amet, consetetur sadip scing elitr, sed diam nonumy</p>
  <div class="rule" style="left:274px;top:117px;width:192px"></div>
  <p class="post" style="top:123px">Lorem ipsum dolor sit amet, consetetur sadip scing elitr, sed diam nonumy</p>
  <div class="rule" style="left:274px;top:161px;width:192px"></div>

  <h4 style="left:511px;top:11px">Write An E-Mail</h4>
  <div class="rule" style="left:511px;top:31px;width:192px"></div>
  <div class="field" style="top:38px;height:23px">Name</div>
  <div class="field" style="top:65px;height:22px">E-Mail</div>
  <div class="field" style="top:92px;height:70px">Comments</div>
  <a class="btn" href="#">SEND</a>
</footer>

<p class="abs copyright">Copyright Statement</p>
</body>
</html>
```